Modern e-Commerce Website for new tea company

We need a web design for a new company called "leaf hollow" based in the UK. We are operating in the food / retailing industry. We are an online retailer of organic Darjeeling Tea (Black and Green Tea) - our clients are end-customers within the UK.

We are looking for a coded wordpress webdesign for a landing page, a potential second page and an online shop.

Target Market(s)

End-customers of tea within the UK

Industry/Entity Type

E-Commerce

Coding

Coded - Design and coding required

Number of Pages Required

3 page

Font styles to use
Other font styles liked:
• Helvetica Neue

Requirements
Must have
• Design expectations:
• We are looking for a very professional looking website. A website that shows the type quality we put into preparing our tea every day. Overall theme of the website should be simplie and clean (white, green). But pictures of tea should be more colourful. Graphics like buttons, text, etc. should be simple, shouldn't stick out too much. Also, don't forget that this website is for people buying tea, so the design should make tea look more appetising.
• Websites that inspire us are:
• https://www.brovanley.co.uk/about-brovanley/brovanley-teas/darjeeling
• - nice colours, icons, graphics
• https://www.plumbrid.com/
• - well designed, simple
• https://www.kelvo.com/
• - simple, clear sections for each point
• How we want each page to be designed
• 1) Landing Page (one-page)
• - sticky menu (header)
• - section 1: slider with pictures of our products
• - section 2: product overview with product pictures
• - section 3: advantages of our products
• - section 4: how our concept works
• - contact us
• - footer (twitter, fb, instagram, disclaimer)
• 2) Second page
• 3) Shop
• Our current site is: http://marpon.sitebox.pw/wp/
Nice to have
• What to avoid
• We want this website to consist of soft colours, so we DON'T want colours that are too hard on the eyes and are "highlighter" like colours. We don't want this website to look too "cartoon like" or too "childish". We are going for a sophisticated, high class look.

```html
<!DOCTYPE html>
<html lang="en">
<head>
<meta charset="utf-8">
<title>Leaf Hollow – Organic Darjeeling Tea</title>
<link href="https://fonts.googleapis.com/css2?family=Questrial&family=Lato:wght@400;700&family=Courgette&display=swap" rel="stylesheet">
<style>
:root{
  --green:#62c644;
  --green-dark:#4aa82f;
  --ink:#333333;
  --muted:#666666;
  --light:#f2f2f2;
  --white:#ffffff;
  --grey-btn:#444444;
  --dark:#2e2e2e;
  --darker:#262626;
  --field:#3a3a3a;
  --line:#dddddd;
}
*{margin:0;padding:0;box-sizing:border-box}
html,body{width:1200px;height:3114px;overflow:hidden}
body{font-family:"Lato",sans-serif;color:var(--ink);background:var(--white);position:relative}
.section{position:absolute;left:0;width:1200px}
.abs{position:absolute}
.title{font-family:"Questrial",sans-serif;font-weight:400;font-size:31px;text-align:center;position:absolute;left:0;width:1200px}
.rule{position:absolute;left:570px;width:60px;height:3px;background:var(--green)}
.rule.white{background:var(--white)}
.btn{display:inline-block;font-family:"Lato",sans-serif;font-weight:700;text-align:center;color:var(--white);border-radius:2px}

/* header */
.site-header{top:0;height:160px;background:var(--white);border-top:7px solid #d8d8d8}
.brand{left:165px;top:38px;display:flex;align-items:center;gap:14px}
.brand-dot{width:62px;height:62px;border-radius:50%;background:var(--ink)}
.brand-name{font-family:"Questrial",sans-serif;font-size:26px;color:var(--ink);letter-spacing:1px}
.contact-bar{left:560px;top:44px;display:flex;align-items:center;gap:26px;font-size:15px}
.contact-bar span{display:flex;align-items:center;gap:8px}
.ic-round{width:22px;height:22px;border-radius:50%;background:var(--green);display:inline-flex;align-items:center;justify-content:center}
.cart{left:965px;top:42px;border:1px solid #ccc;padding:4px 8px;font-size:14px;display:flex;align-items:center;gap:6px}
.main-nav{left:540px;top:108px;display:flex;align-items:center;font-size:15px;color:#555}
.main-nav a{padding:0 17px;line-height:35px;text-decoration:none;color:#555}
.main-nav a.active{background:var(--green);color:var(--white);font-weight:700;padding:0 18px}
.caret{font-size:10px;color:#aaa;margin-left:4px}

/* hero */
.hero{top:160px;height:411px;background:linear-gradient(180deg,#7f95a8 0%,#5f7a70 40%,#9aa7a0 78%,#dcdcdc 100%)}
.hero-art{position:absolute;left:640px;top:70px;width:440px;height:300px;border-radius:30px;background:radial-gradient(ellipse at 45% 55%,#c97e1b 0%,#b06a12 35%,rgba(230,230,230,.6) 62%,rgba(255,255,255,0) 75%)}
.hero-copy{left:170px;top:92px;width:370px;text-align:center;color:var(--white)}
.hero-kicker{font-size:18px}
.hero-title{font-family:"Courgette",cursive;font-size:38px;margin-top:14px}
.hero-sub{font-size:16px;line-height:26px;margin-top:14px}
.hero-btns{margin-top:22px;display:flex;justify-content:center;gap:24px}
.hero-btns .btn{width:104px;line-height:30px;font-size:14px}
.btn-grey{background:var(--grey-btn)}
.btn-green{background:var(--green)}
.dots{left:314px;top:336px;display:flex;gap:14px}
.dots i{width:12px;height:12px;border-radius:50%;background:var(--white);display:block}
.dots i.on{background:var(--green)}

/* welcome */
.welcome{top:571px;height:227px;background:var(--light)}
.welcome .title{top:32px}
.welcome .rule{top:86px}
.welcome p{position:absolute;left:190px;width:820px;top:112px;text-align:center;font-size:13.5px;line-height:25px;color:#444}
.welcome p a{color:var(--green);text-decoration:underline}

/* teas */
.teas{top:798px;height:514px;background:linear-gradient(180deg,#2f4a2a 0%,#3c5a2f 50%,#2b4325 100%)}
.teas .title{top:28px;color:var(--white)}
.teas .rule{top:80px}
.tea-card{position:absolute;top:115px;width:241px;height:340px;background:var(--white);border-radius:3px;text-align:center}
.tea-img{width:112px;height:112px;border-radius:50%;margin:16px auto 0}
.tea-card h3{font-family:"Questrial",sans-serif;font-weight:400;font-size:21px;margin-top:28px}
.tea-card .type{font-size:13.5px;margin-top:8px;color:#444}
.tea-card .desc{font-size:10.5px;line-height:16px;color:#666;width:200px;margin:12px auto 0}
.tea-card .price{font-weight:700;font-size:17px;margin-top:14px}
.tea-card .btn{width:116px;line-height:24px;font-size:12px;background:var(--green);color:#222;margin-top:12px}

/* features */
.features{top:1312px;height:534px;background:var(--light)}
.features .title{top:38px}
.features .rule{top:90px}
.feature-art{left:190px;top:175px;width:250px;height:310px;border-radius:120px 120px 40px 60px;background:linear-gradient(160deg,#d9d9d9,#c9c9c9)}
.feature-arc{left:340px;top:130px}
.feature{position:absolute;left:527px;display:flex;gap:18px;width:520px}
.f-icon{flex:none;width:66px;height:66px;border-radius:50%;background:var(--white);border:3px solid var(--ink);display:flex;align-items:center;justify-content:center}
.f-icon i{width:50px;height:50px;border-radius:50%;background:var(--green);display:flex;align-items:center;justify-content:center}
.feature h4{font-family:"Lato",sans-serif;font-size:15px;color:#333;margin-top:4px}
.feature p{font-size:11.5px;line-height:18px;color:#555;margin-top:8px}

/* concept */
.concept{top:1846px;height:462px;background:linear-gradient(180deg,#3e5a36 0%,#4c6e3a 45%,#36502c 100%)}
.concept .title{top:66px;color:var(--white)}
.concept .rule{top:118px}
.step{position:absolute;top:190px;width:210px;text-align:center;color:var(--white)}
.step h4{font-family:"Lato",sans-serif;font-size:19px;margin-top:22px}
.step p{font-size:12px;line-height:22px;margin-top:12px}

/* reviews */
.reviews{top:2308px;height:317px;background:#f4f4f4}
.reviews .title{top:42px}
.reviews .rule{top:94px}
.arrow{position:absolute;top:184px;width:24px;height:24px;border-radius:50%;display:flex;align-items:center;justify-content:center}
.review{position:absolute;top:150px;width:460px}
.avatar{position:absolute;left:0;top:0;width:80px;height:80px;border-radius:50%;border:4px solid var(--green);background:linear-gradient(160deg,#b9c7d3,#8596a5)}
.pin{position:absolute;left:28px;top:78px;width:0;height:0;border-left:12px solid transparent;border-right:12px solid transparent;border-top:16px solid var(--green)}
.review blockquote{position:absolute;left:120px;top:10px;width:330px;font-size:11.5px;line-height:20px;color:#555;text-indent:30px}
.quote-mark{position:absolute;left:96px;top:-2px;font-family:Georgia,serif;font-size:40px;color:#ccc}
.quote-end{position:absolute;left:312px;top:84px;font-family:Georgia,serif;font-size:40px;color:#ccc}
.review cite{position:absolute;left:6px;top:112px;font-style:normal;font-size:12px;font-weight:700}
.divider{position:absolute;left:598px;top:140px;width:1px;height:140px;background:var(--line)}

/* contact */
.contact{top:2625px;height:360px;background:var(--dark);color:var(--white)}
.contact .title{top:30px;color:var(--white)}
.contact .rule{top:82px}
.col-h{position:absolute;top:104px;font-family:"Lato",sans-serif;font-size:17px;font-weight:400}
.field{position:absolute;left:188px;width:255px;height:22px;background:var(--field);font-size:10px;color:#bbb;padding:5px 8px}
.send{position:absolute;left:188px;top:303px;width:84px;line-height:24px;font-size:12px;background:var(--green);color:#222}
.map{left:493px;top:140px;width:257px;height:158px;background:linear-gradient(135deg,#ece6d4,#e2dcc6);border:3px solid #555}
.col-sep{position:absolute;top:104px;width:1px;height:220px;background:#444}
.info{position:absolute;left:803px;width:210px;font-size:11px;line-height:16px;display:flex;gap:10px;align-items:flex-start}
.social{position:absolute;left:803px;top:272px;display:flex;gap:8px}
.social i{width:24px;height:24px;border-radius:50%;background:var(--white);display:block}

/* newsletter */
.newsletter{top:2985px;height:85px;background:var(--green)}
.nl-icon{left:185px;top:20px;width:46px;height:46px;border-radius:50%;border:3px solid #222;display:flex;align-items:center;justify-content:center}
.nl-text{left:242px;top:27px;font-family:"Questrial",sans-serif;font-size:24px;color:#222}
.nl-input{left:512px;top:25px;width:323px;height:34px;background:var(--white);font-size:11px;color:#999;padding:11px 12px}
.nl-btn{left:848px;top:25px;width:164px;line-height:34px;background:var(--darker);font-size:15px;letter-spacing:1px}

.site-footer{top:3070px;height:44px;background:var(--darker);color:#bbb;font-size:11px;text-align:center;line-height:44px}
</style>
</head>
<body>

<header class="section site-header">
  <div class="abs brand"><span class="brand-dot"></span><span class="brand-name">LEAF HOLLOW</span></div>
  <div class="abs contact-bar">
    <span><i class="ic-round"><svg width="12" height="12" viewBox="0 0 24 24"><path fill="#fff" d="M6.6 10.8a15 15 0 006.6 6.6l2.2-2.2c.3-.3.7-.4 1-.2 1.1.4 2.3.6 3.6.6.6 0 1 .4 1 1V20c0 .6-.4 1-1 1A17 17 0 013 4c0-.6.4-1 1-1h3.5c.6 0 1 .4 1 1 0 1.3.2 2.5.6 3.6.1.3 0 .7-.2 1z"/></svg></i>+44 1632 960 418</span>
    <span><i class="ic-round"><svg width="12" height="10" viewBox="0 0 24 18"><rect x="1" y="1" width="22" height="16" rx="2" fill="#fff"/><path d="M2 2l10 8 10-8" stroke="#62c644" stroke-width="2" fill="none"/></svg></i>info@leafhollow.co.uk</span>
  </div>
  <div class="abs cart"><svg width="18" height="16" viewBox="0 0 24 20"><path d="M1 2h4l3 11h12l3-8H7" stroke="#333" stroke-width="2" fill="none"/><circle cx="9" cy="17" r="2" fill="#333"/><circle cx="18" cy="17" r="2" fill="#333"/></svg>£ 0.00</div>
  <nav class="abs main-nav">
    <a class="active" href="#">Home</a>
    <a href="#">Shop</a>
    <a href="#">Darjeeling<span class="caret">⌵</span></a>
    <a href="#">Pure &amp; Organic<span class="caret">⌵</span></a>
    <a href="#">About Us<span class="caret">⌵</span></a>
  </nav>
</header>

<section class="section hero">
  <div class="hero-art" role="img" aria-label="Glass cup of amber green tea on a saucer against a misty hillside"></div>
  <div class="abs hero-copy">
    <div class="hero-kicker">New Arrival. 100% Organic.</div>
    <div class="hero-title">Darjeeling Green Tea</div>
    <div class="hero-sub">Try our freshly arrived Darjeeling Green Tea.<br>FTGFOP-1.</div>
    <div class="hero-btns"><span class="btn btn-grey">Read More</span><span class="btn btn-green">Order Now</span></div>
  </div>
  <div class="abs dots"><i class="on"></i><i></i><i></i></div>
</section>

<section class="section welcome">
  <h2 class="title">Welcome To Leaf Hollow</h2>
  <div class="rule"></div>
  <p>Lorem ipsum dolor sit amet, consectetuer adipiscing elit, sed diam nonummy nibh euismod tincidunt ut laoreet dolore magna aliquam erat volutpat. Ut wisi enim ad minim veniam, quis nostrud exerci tation ullamcorper suscipit lobortis nisl ut aliquip ex ea commodo consequat. Duis autem vel eum iriure dolor. Ut wisi enim ad minim veniam, quis nostrud exerci tation ullamcorper suscipit consequat. <a href="#">Read More</a></p>
</section>

<section class="section teas" role="img" aria-label="Tea pickers among terraced tea bushes">
  <h2 class="title">Our Darjeeling Teas</h2>
  <div class="rule white"></div>
  <article class="tea-card" style="left:193px">
    <div class="tea-img" role="img" aria-label="Dry first flush leaves beside a cup of golden tea" style="background:linear-gradient(90deg,#6b6350 50%,#e39a14 50%)"></div>
    <h3>First Flush 2016</h3>
    <div class="type">Black, Organic Darjeeling Tea</div>
    <p class="desc">Our most popular Darjeeling Tea. An organic First Flush from the 2016 harvest with the highest gradation: FTGFOP-1.</p>
    <div class="price">£19.99 (for 500g)</div>
    <span class="btn">Order Now</span>
  </article>
  <article class="tea-card" style="left:479px">
    <div class="tea-img" role="img" aria-label="Dry second flush leaves beside a cup of copper tea" style="background:linear-gradient(90deg,#4d3a2c 50%,#b4461a 50%)"></div>
    <h3>Second Flush 2016</h3>
    <div class="type">Black, Organic Darjeeling Tea</div>
    <p class="desc">A Second Flush from 2016 with the highest leaf grade: FTGFOP-1. From 100% organic cultivation, certified by the Green Field Trust.</p>
    <div class="price">£19.99 (for 500g)</div>
    <span class="btn">Order Now</span>
  </article>
  <article class="tea-card" style="left:765px">
    <div class="tea-img" role="img" aria-label="Dry green tea leaves beside a cup of amber tea" style="background:linear-gradient(90deg,#4a4038 50%,#c2541c 50%)"></div>
    <h3>Green Tea</h3>
    <div class="type">Organic Darjeeling Tea</div>
    <p class="desc">Try our new Green Darjeeling Tea. An organic First Flush from the 2016 harvest with the highest gradation: FTGFOP-1.</p>
    <div class="price">£14.99 (for 500g)</div>
    <span class="btn">Order Now</span>
  </article>
</section>

<section class="section features">
  <h2 class="title">Key Features</h2>
  <div class="rule"></div>
  <div class="abs feature-art" role="img" aria-label="Soft grey illustration of a woman holding a tea leaf"></div>
  <svg class="abs feature-arc" width="120" height="380" viewBox="0 0 120 380"><path d="M20 10 A200 200 0 0 1 20 370" stroke="#62c644" stroke-width="7" fill="none"/></svg>
  <div class="feature" style="top:120px">
    <div class="f-icon"><i><svg width="26" height="26" viewBox="0 0 24 24"><path fill="#fff" d="M12 2l2.9 6 6.6.9-4.8 4.6 1.2 6.5L12 17l-5.9 3 1.2-6.5L2.5 8.9 9.1 8z"/></svg></i></div>
    <div><h4>Highest Quality</h4><p>We ensure you get First and Second Flush Teas with the highest leaf gradation: FTGFOP-1. Tasted by one of UK's most renowned tea tasters.</p></div>
  </div>
  <div class="feature" style="top:212px">
    <div class="f-icon"><i><svg width="26" height="26" viewBox="0 0 24 24"><path fill="#fff" d="M20 3C9 3 4 9 4 16c0 2 1 4 1 4l1-1c1-5 5-9 10-11-4 3-7 6-8 11 9 0 12-7 12-16z"/></svg></i></div>
    <div><h4>100% Organic</h4><p>All our tea is from certified organic production. Inspected by internationally reputable service providers.</p></div>
  </div>
  <div class="feature" style="top:305px">
    <div class="f-icon"><i><svg width="26" height="26" viewBox="0 0 24 24"><circle cx="10" cy="10" r="6" stroke="#fff" stroke-width="2.5" fill="none"/><path d="M14.5 14.5L21 21" stroke="#fff" stroke-width="3"/></svg></i></div>
    <div><h4>Full Transparency</h4><p>Look up pesticide analysis results of your tea and find out from which Darjeeling tea estate your tea came from by using the batch number of your tea package.</p></div>
  </div>
  <div class="feature" style="top:413px">
    <div class="f-icon"><i><svg width="26" height="26" viewBox="0 0 24 24"><circle cx="12" cy="12" r="10" fill="#fff"/><text x="12" y="17" text-anchor="middle" font-family="Lato,sans-serif" font-weight="700" font-size="13" fill="#62c644">£</text></svg></i></div>
    <div><h4>Low Price</h4><p>We did everything to eliminate all unnecessary costs in order to provide you the lowest possible price.</p></div>
  </div>
</section>

<section class="section concept" role="img" aria-label="Terraced green tea plantation hills at dusk">
  <h2 class="title">Our Concept</h2>
  <div class="rule white"></div>
  <div class="step" style="left:158px">
    <svg width="76" height="64" viewBox="0 0 76 64"><path d="M8 20h60v40H8z" fill="#62c644"/><path d="M8 20l10-14h40l10 14" fill="#7bd65d"/><path d="M30 34h16v10H30z" fill="#3e5a36"/></svg>
    <h4>Large Packages</h4>
    <p>By Using Large Packets (500g, 1000g), We Can Save On Packaging, Labeling And Handling Costs.</p>
  </div>
  <div class="step" style="left:382px">
    <svg width="76" height="64" viewBox="0 0 76 64"><path d="M4 22l16-10 18 10 18-10 16 10-8 16-26 14-26-14z" fill="#62c644"/><path d="M26 30l12 8 12-8" stroke="#3e5a36" stroke-width="3" fill="none"/></svg>
    <h4>Direct Trade</h4>
    <p>We Cut All Middlemen And Buy Directly From The Leaf Hollow In Darjeeling.</p>
  </div>
  <div class="step" style="left:601px">
    <svg width="76" height="64" viewBox="0 0 76 64"><rect x="14" y="28" width="12" height="32" fill="#62c644"/><path d="M30 60V28l10-22c5 0 7 4 6 9l-3 11h17c4 0 6 4 5 7l-6 22c-1 3-3 5-6 5z" fill="#62c644"/></svg>
    <h4>Simplicity</h4>
    <p>We Only Sell 100% Organic High Grad FTGFOP-1 Darjeeling Tea To Reduce Costs. Nothing Else.</p>
  </div>
  <div class="step" style="left:830px">
    <svg width="76" height="64" viewBox="0 0 76 64"><rect x="10" y="10" width="56" height="50" rx="3" fill="#62c644"/><rect x="10" y="10" width="56" height="12" fill="#4aa82f"/><g fill="#3e5a36"><rect x="17" y="28" width="8" height="7"/><rect x="29" y="28" width="8" height="7"/><rect x="41" y="28" width="8" height="7"/><rect x="53" y="28" width="8" height="7"/><rect x="17" y="40" width="8" height="7"/><rect x="29" y="40" width="8" height="7"/><rect x="41" y="40" width="8" height="7"/><rect x="53" y="40" width="8" height="7"/></g><rect x="20" y="4" width="5" height="12" fill="#62c644"/><rect x="51" y="4" width="5" height="12" fill="#62c644"/></svg>
    <h4>One Year's Supply</h4>
    <p>Tea Stores Well For Long Periods Of Time. Therefore Many Of Our Customers Buy Their Year's Supply At A Time. This Reduces Shipping Costs.</p>
  </div>
</section>

<section class="section reviews">
  <h2 class="title">Customer Reviews</h2>
  <div class="rule"></div>
  <span class="arrow" style="left:113px;border:2px solid #555"><svg width="10" height="10" viewBox="0 0 10 10"><path d="M7 1L3 5l4 4" stroke="#555" stroke-width="2" fill="none"/></svg></span>
  <span class="arrow" style="left:1056px;border:2px solid var(--green)"><svg width="10" height="10" viewBox="0 0 10 10"><path d="M3 1l4 4-4 4" stroke="#62c644" stroke-width="2" fill="none"/></svg></span>
  <div class="review" style="left:178px">
    <div class="avatar" role="img" aria-label="Customer portrait"></div><div class="pin"></div>
    <span class="quote-mark">“</span>
    <blockquote>Lorem ipsum sit amet co adipiscing elit euismo dtepor incidunt ut la dolore ma aliquamei kni minim niim veni exercitation ullamco ips sllitosei ameti co adipiscing elitsed do eiusmod te epo uom Accusant dol oremque laudantium.</blockquote>
    <span class="quote-end">”</span>
    <cite>- Tom Reed</cite>
  </div>
  <div class="divider"></div>
  <div class="review" style="left:642px">
    <div class="avatar" role="img" aria-label="Customer portrait"></div><div class="pin"></div>
    <span class="quote-mark">“</span>
    <blockquote>Lorem ipsum sit amet co adipiscing elit euismo dtepor incidunt ut la dolore ma aliquamei kni minim niim veni exercitation ullamco ips sllitosei ameti co adipiscing elitsed do eiusmod te epo uom Accusant dol oremque laudantium.</blockquote>
    <span class="quote-end">”</span>
    <cite>- Mara Quill</cite>
  </div>
</section>

<section class="section contact">
  <h2 class="title">Contact Details</h2>
  <div class="rule"></div>
  <h3 class="col-h" style="left:188px">Quick Inquiry</h3>
  <div class="field" style="top:140px">Name</div>
  <div class="field" style="top:167px">Email</div>
  <div class="field" style="top:194px">Subject</div>
  <div class="field" style="top:221px;height:70px">Message</div>
  <span class="btn send">SEND</span>
  <div class="col-sep" style="left:468px"></div>
  <h3 class="col-h" style="left:493px">Location Map</h3>
  <div class="abs map" role="img" aria-label="Street map showing the shop location"></div>
  <div class="col-sep" style="left:778px"></div>
  <h3 class="col-h" style="left:803px">Contact Details</h3>
  <div class="info" style="top:136px"><svg width="10" height="14" viewBox="0 0 10 14"><path d="M5 0a5 5 0 015 5c0 4-5 9-5 9S0 9 0 5a5 5 0 015-5z" fill="#62c644"/><circle cx="5" cy="5" r="2" fill="#2e2e2e"/></svg><span>Lorem ipsum dolor sit amet, consectetur adipiscing elit fusce quis justo ut arcu scelerisque - 123456</span></div>
  <div class="info" style="top:194px"><svg width="12" height="12" viewBox="0 0 24 24"><path fill="#62c644" d="M6.6 10.8a15 15 0 006.6 6.6l2.2-2.2c.3-.3.7-.4 1-.2 1.1.4 2.3.6 3.6.6.6 0 1 .4 1 1V20c0 .6-.4 1-1 1A17 17 0 013 4c0-.6.4-1 1-1h3.5c.6 0 1 .4 1 1 0 1.3.2 2.5.6 3.6.1.3 0 .7-.2 1z"/></svg><span>+44 1632 960 418</span></div>
  <div class="info" style="top:220px"><svg width="12" height="12" viewBox="0 0 24 24"><path fill="#62c644" d="M6.6 10.8a15 15 0 006.6 6.6l2.2-2.2c.3-.3.7-.4 1-.2 1.1.4 2.3.6 3.6.6.6 0 1 .4 1 1V20c0 .6-.4 1-1 1A17 17 0 013 4c0-.6.4-1 1-1h3.5c.6 0 1 .4 1 1 0 1.3.2 2.5.6 3.6.1.3 0 .7-.2 1z"/></svg><span>+44 1632 960 418</span></div>
  <div class="info" style="top:246px"><svg width="13" height="10" viewBox="0 0 24 18"><rect x="1" y="1" width="22" height="16" rx="2" fill="#62c644"/><path d="M2 2l10 8 10-8" stroke="#2e2e2e" stroke-width="2" fill="none"/></svg><span>info@leafhollow.co.uk</span></div>
  <div class="social"><i></i><i></i><i></i><i></i></div>
</section>

<section class="section newsletter">
  <div class="abs nl-icon"><svg width="22" height="16" viewBox="0 0 24 18"><rect x="1" y="1" width="22" height="16" rx="2" fill="#222"/><path d="M2 2l10 8 10-8" stroke="#62c644" stroke-width="2" fill="none"/></svg></div>
  <div class="abs nl-text">Sign Up For Newsletter</div>
  <div class="abs nl-input">Enter your email here</div>
  <span class="abs btn nl-btn">SUBSCRIBE</span>
</section>

<footer class="section site-footer">Copyright © 2016 Leaf Hollow. All Rights Reserved.</footer>

</body>
</html>
```